International freight forwarder experienced in perishable handling needs a web design

We need a website designed that will allow us to capture more customers through the website. We would like a visually appealing design that is not so heavy on text. Our business covers the logistics and freight forwarding industries and we have offices in South America and the USA. Our main customers are importers USA, Europe, Asia and Russia and we currently work almost exclusively with perishable products such as fresh cut flowers, fresh exotics fruits, cacao, fresh fish etc. We would like to convey a fresh, modern approach to freight forwarding focusing on concepts such as - time sensitive, anytime-anywhere delivery, innovation, experience, reliability and confidence. Should include links with Plumetta and Worvanet. Our core solutions include: Core Services
*Air Freight
*Ocean Freight
*Warehousing & Distribution
Our industry solutions cover
*Flowers
*FMCG including, fruits, vegetables
*Live animals
*Automotive
*Consumer Goods
*Industrial
*Oil & Gas
*Pharma
* Event logistics
* Project logistics

Target Market(s)

Importers in Europe, USA, Asia, Middle East and Russia

Number of Pages Required

4 page

Font styles to use
Sans Serif

Colors
a1cd39
606060
000000

Requirements
Must have
• Photos of fresh cut flowers, FMCG such as cacao, fresh fish (packaged for shipping), fresh exotic fruits, pharma products (packaged for shipping), oil and gas etc. Internal customer login access
Nice to have
• Photos of cargo shipping carriers and cargo airline carriers. Features similar to those of following website http://www.brolvacargo.com/eng/main/index.jsp?FromURL=web
Should not have
• Too much text, needs to be visually pleasing

```html
<!DOCTYPE html>
<html lang="en">
<head>
<meta charset="utf-8">
<title>Vantrelo Alliance Group – Freight Services</title>
<link href="https://fonts.googleapis.com/css2?family=Roboto+Condensed:wght@400;700&family=Open+Sans:ital,wght@0,400;0,600;1,400&display=swap" rel="stylesheet">
<style>
:root{
  --green:#a1cd39;
  --green-deep:#5f9a1c;
  --green-card:rgba(110,165,30,.9);
  --grey:#606060;
  --ink:#000000;
  --dark:#262626;
  --dark-2:#1b1b1b;
  --white:#ffffff;
  --text:#333333;
}
*{margin:0;padding:0;box-sizing:border-box}
html,body{width:774px;height:1200px;overflow:hidden;background:var(--white)}
body{font-family:"Open Sans",sans-serif;color:var(--text);position:relative}
.page{position:relative;width:774px;height:1200px;overflow:hidden}
.abs{position:absolute}

/* top nav */
.topnav{top:0;left:0;width:774px;height:14px;background:linear-gradient(#fff,#ececec);display:flex;justify-content:center;align-items:center;gap:6px;font:700 6.2px "Roboto Condensed",sans-serif;color:#333;text-transform:uppercase}
.topnav .sep{color:var(--green)}
.header{top:14px;left:0;width:774px;height:44px;background:var(--white)}
.follow{left:173px;top:15px;display:flex;align-items:center;gap:3px;font:700 6.4px "Roboto Condensed",sans-serif;color:#333}
.follow span.lbl{margin-right:3px}
.social{height:15px;padding:0 4px;border-radius:4px;background:#3f64a8;color:#fff;font:700 5.6px "Roboto Condensed",sans-serif;display:flex;align-items:center}
.social.tw{background:#39a9e0}.social.in{background:#1c74b0}
.brand{left:321px;top:10px;display:flex;align-items:center;gap:5px}
.brand .dot{width:22px;height:22px;border-radius:50%;background:var(--green)}
.brand .name{font:700 15px "Roboto Condensed",sans-serif;color:#333;line-height:1}
.brand .sub{font:400 4.5px "Open Sans",sans-serif;color:#888;letter-spacing:1px;margin-top:1px;text-align:right}
.tools{left:516px;top:13px;display:flex;gap:4px}
.tool{height:18px;border:1.5px solid var(--green);border-radius:9px;font:700 6px "Roboto Condensed",sans-serif;display:flex;align-items:center;justify-content:center;color:#333;padding:0 7px}
.tool svg{width:8px;height:8px}

/* hero */
.hero{top:58px;left:0;width:774px;height:278px}
.hero-photo{position:absolute;inset:0;background:linear-gradient(180deg,#9fb9d2 0%,#c9d4dc 30%,#b9b3a7 60%,#6f6a60 100%)}
.hero-kicker{top:33px;width:774px;text-align:center;font:700 10px "Roboto Condensed",sans-serif;color:#8abd26}
.hero-title{top:50px;width:774px;text-align:center;font:700 21px/20px "Roboto Condensed",sans-serif;color:#2b2b2b}
.svc{top:138px;width:134px;height:118px;background:var(--green-card);padding:13px 15px;color:#fff}
.svc h3{font:700 10px/9.5px "Roboto Condensed",sans-serif;text-transform:uppercase;margin-bottom:8px;min-height:10px}
.svc p{font-size:4.8px;line-height:8px}
.btn{display:inline-block;border:1px solid #fff;color:#fff;font:700 5.6px "Open Sans",sans-serif;padding:3px 6px;line-height:6px}

/* solutions */
.solutions{top:336px;left:0;width:774px;height:263px;background:radial-gradient(ellipse at 50% 40%,#333 0%,var(--dark) 55%,var(--dark-2) 100%)}
.map{position:absolute;left:70px;top:40px;width:640px;height:190px;border-radius:40%;background:rgba(255,255,255,.025)}
.sec-title{width:774px;text-align:center;font:700 15px "Roboto Condensed",sans-serif;text-transform:uppercase}
.rule{left:330px;width:114px;height:6px}
.sol{top:94px;width:123px;height:118px;border:1px solid var(--green);padding:10px 9px 0 9px;color:#ddd}
.sol .head{display:flex;gap:5px;align-items:flex-start}
.sol svg{width:11px;height:11px;flex:none}
.sol h4{font:700 8px/8px "Roboto Condensed",sans-serif;color:var(--green);text-transform:uppercase;margin-top:2px}
.sol p{font-size:4.4px;line-height:7.1px;margin:3px 0 0 16px;width:88px}
.sol .btn{position:absolute;left:25px;top:96px}
.dots{top:222px;left:0;width:774px;display:flex;justify-content:center;gap:3px}
.dots i{width:4px;height:4px;border-radius:50%;background:#fff}

/* testimonials */
.testi{top:599px;left:0;width:774px;height:251px;background:#fafafa}
.people{left:410px;top:20px;width:364px;height:231px;background:linear-gradient(120deg,#f4f4f4 0%,#6b5a45 30%,#3a3a3a 60%,#4a6b8f 100%);clip-path:polygon(18% 0,100% 0,100% 100%,5% 100%)}
.avatar{left:262px;top:67px;width:66px;height:65px;background:linear-gradient(#6e8a62,#c69a7a);border:2px solid #333}
.quote{left:190px;top:143px;width:214px;text-align:center;font:italic 6.2px/8.6px "Open Sans",sans-serif;color:#333}
.who{left:190px;top:200px;width:214px;text-align:center}
.who b{display:block;font:700 7px/8px "Roboto Condensed",sans-serif;color:#222}
.who div{font-size:5px;line-height:6px;color:#333;margin-top:1px}
.tdots{left:280px;top:228px;display:flex;gap:2px}
.tdots i{width:5px;height:5px;border-radius:50%;border:1px solid #999}
.tdots i.on{background:#999}

/* news */
.news{top:850px;left:0;width:774px;height:196px;background:linear-gradient(180deg,#7cb82a,#5a9a18)}
.news-title{top:25px;width:774px;text-align:center;color:#fff;font:700 17px "Roboto Condensed",sans-serif}
.news-sub{top:45px;width:774px;text-align:center;color:#fff;font:400 6.5px "Roboto Condensed",sans-serif}
.item{top:73px;width:145px;color:#fff}
.item h5{font:700 11px/12.5px "Roboto Condensed",sans-serif;text-transform:uppercase}
.item p{font-size:4.6px;line-height:8.2px;margin:6px 0 9px;color:#eef6df}

/* footer */
.footer{top:1046px;left:0;width:774px;height:154px;background:linear-gradient(#222,#161616);color:#ccc}
.fh{font:700 6.8px "Roboto Condensed",sans-serif;color:var(--green);text-transform:uppercase}
.ftext{font-size:4.8px;line-height:7.8px;color:#ddd}
.links{list-style:none;font:400 5px/9.2px "Open Sans",sans-serif;color:#ddd;text-transform:uppercase}
.links li:before{content:"• ";color:var(--green)}
.news-form{left:466px;top:92px;width:134px;height:12px;border:1px solid var(--green);display:flex}
.news-form span{flex:1;font-size:5px;color:#fff;padding:3px 5px}
.news-form b{width:39px;border-left:1px solid var(--green);font:400 5px "Open Sans",sans-serif;color:var(--green);padding:3px 6px}
.fline{top:114px;left:173px;width:428px;height:1px;background:#3a3a3a}
.copy{top:130px;left:173px;font-size:4.8px;color:#ddd}
.copy em{font-style:normal;color:var(--green)}
</style>
</head>
<body>
<div class="page">

  <nav class="abs topnav">
    <span>Our Company</span><span class="sep">/</span>
    <span>Freight Forwarding Services</span><span class="sep">/</span>
    <span>Industry Specific Solutions</span><span class="sep">/</span>
    <span>Express</span><span class="sep">/</span>
    <span>Innovation</span><span class="sep">/</span>
    <span>Contact Us</span>
  </nav>

  <header class="abs header">
    <div class="abs follow">
      <span class="lbl">FOLLOW <span style="color:var(--green)">US</span></span>
      <span class="social">Plumetta</span>
      <span class="social tw">Tweelo</span>
      <span class="social in">Worvanet</span>
    </div>
    <div class="abs brand">
      <span class="dot"></span>
      <div><div class="name">Vantrelo Alliance</div><div class="sub">GROUP</div></div>
    </div>
    <div class="abs tools">
      <span class="tool">LOGIN&nbsp;<svg viewBox="0 0 10 10"><circle cx="4" cy="4" r="2.6" fill="none" stroke="#a1cd39" stroke-width="1.4"/><path d="M6 6l3 3" stroke="#a1cd39" stroke-width="1.4"/></svg></span>
      <span class="tool" style="width:20px;padding:0"><svg viewBox="0 0 10 10"><circle cx="4" cy="4" r="2.8" fill="none" stroke="#555" stroke-width="1.2"/><path d="M6 6l3 3" stroke="#555" stroke-width="1.2"/></svg></span>
      <span class="tool" style="width:20px;padding:0"><svg viewBox="0 0 12 8" style="width:10px"><rect width="8" height="6" y="1" fill="#c33"/><rect width="8" height="1" y="3" fill="#fff"/><rect width="3.5" height="3" y="1" fill="#2a4b9b"/><path d="M9 3l1.5 2L12 3z" fill="#555"/></svg></span>
    </div>
  </header>

  <section class="abs hero">
    <div class="hero-photo" role="img" aria-label="Cargo airplane on the apron being loaded with pallets of fresh produce"></div>
    <div class="abs hero-kicker">BUSINESS TO VANTRELO ALLIANCE GROUP</div>
    <h1 class="abs hero-title">PROVIDING FIRST CLASS<br>FREIGHT SERVICES</h1>

    <article class="abs svc" style="left:174px">
      <h3>Air Freight</h3>
      <p>Lorem Ipsum has been the industry's standard dummy text ever since the 1500s, when an unknown printer took a galley of type and scrambled it to make a type specimen book.</p>
      <span class="btn" style="margin-top:8px">Read More</span>
    </article>
    <article class="abs svc" style="left:320px">
      <h3>Ocean Freight</h3>
      <p>Lorem Ipsum has been the industry's standard dummy text ever since the 1500s, when an unknown printer took a galley of type and scrambled it to make a type specimen book.</p>
      <span class="btn" style="margin-top:8px">Read More</span>
    </article>
    <article class="abs svc" style="left:466px">
      <h3>Warehousing<br>&amp; Distribution</h3>
      <p>Lorem Ipsum has been the industry's standard dummy text ever since the 1500s, when an unknown printer took a galley of type and scrambled it to make a type</p>
      <span class="btn" style="margin-top:12px">Read More</span>
    </article>
  </section>

  <section class="abs solutions">
    <div class="map" role="img" aria-label="Faint world map backdrop"></div>
    <h2 class="abs sec-title" style="top:34px;color:#fff">Our Industry Solutions Cover</h2>
    <svg class="abs rule" style="top:56px" viewBox="0 0 114 6"><path d="M0 1H50L57 5L64 1H114" fill="none" stroke="#a1cd39" stroke-width="1"/></svg>

    <svg class="abs" style="left:165px;top:143px" width="8" height="20" viewBox="0 0 8 20"><path d="M7 1L1 10L7 19" fill="none" stroke="#a1cd39" stroke-width="1.2"/></svg>
    <svg class="abs" style="left:601px;top:143px" width="8" height="20" viewBox="0 0 8 20"><path d="M1 1L7 10L1 19" fill="none" stroke="#a1cd39" stroke-width="1.2"/></svg>

    <article class="abs sol" style="left:186px">
      <div class="head"><svg viewBox="0 0 12 12"><path d="M3 2c0 3 1.5 5 3 5s3-2 3-5l-1.5 1.5L6 1 4.5 3.5zM6 7v4M3.5 9.5c1 0 2.5 1 2.5 1.5M8.5 9.5c-1 0-2.5 1-2.5 1.5" fill="none" stroke="#a1cd39" stroke-width=".9"/></svg><h4>Flowers</h4></div>
      <p>Lorem ipsum dolor sit amet, consectetur adipisicing elit, sed do eiusmod tempor incididunt ut labore et dolore magna aliqua. Ut enim ad minim veniam, quis nostrud exercitation ullamco laboris nisi ut aliquip ex ea commodo consequat. Duis aute irure dolor in reprehenderit in voluptate velit esse cillum.</p>
      <span class="btn">Read More</span>
    </article>
    <article class="abs sol" style="left:326px">
      <div class="head"><svg viewBox="0 0 12 12"><path d="M2 10c2-1 6-4 7-7l2-2M9 3c1 1 1 2 0 3M6 4l1 1M4 6l1 1" fill="none" stroke="#a1cd39" stroke-width=".9"/></svg><h4>FMCG Including,<br>Fruits, Vegetables</h4></div>
      <p>Lorem ipsum dolor sit amet, consectetur adipisicing elit, sed do eiusmod tempor incididunt ut labore et dolore magna aliqua. Ut enim ad minim veniam, quis nostrud exercitation ullamco laboris nisi ut aliquip ex ea commodo consequat. Duis aute irure dolor in reprehenderit.</p>
      <span class="btn">Read More</span>
    </article>
    <article class="abs sol" style="left:465px">
      <div class="head"><svg viewBox="0 0 12 12"><ellipse cx="6" cy="8" rx="2.6" ry="2.2" fill="none" stroke="#a1cd39" stroke-width=".9"/><circle cx="2.3" cy="5" r="1.1" fill="none" stroke="#a1cd39" stroke-width=".8"/><circle cx="4.5" cy="2.6" r="1.1" fill="none" stroke="#a1cd39" stroke-width=".8"/><circle cx="7.5" cy="2.6" r="1.1" fill="none" stroke="#a1cd39" stroke-width=".8"/><circle cx="9.7" cy="5" r="1.1" fill="none" stroke="#a1cd39" stroke-width=".8"/></svg><h4>Live Animals</h4></div>
      <p>Lorem ipsum dolor sit amet, consectetur adipisicing elit, sed do eiusmod tempor incididunt ut labore et dolore magna aliqua. Ut enim ad minim veniam, quis nostrud exercitation ullamco laboris nisi ut aliquip ex ea commodo consequat. Duis aute irure dolor in reprehenderit.</p>
      <span class="btn">Read More</span>
    </article>

    <div class="abs dots"><i></i><i></i><i></i><i></i><i></i></div>
  </section>

  <section class="abs testi">
    <div class="abs people" role="img" aria-label="Two delivery staff in green caps carrying parcels beside a blue truck"></div>
    <h2 class="abs sec-title" style="top:28px;left:0;color:#2b2b2b">What Customers Are Saying About Us</h2>
    <svg class="abs rule" style="top:50px" viewBox="0 0 114 6"><path d="M0 1H50L57 5L64 1H114" fill="none" stroke="#a1cd39" stroke-width="1"/></svg>
    <div class="abs avatar" role="img" aria-label="Portrait of the quoted customer"></div>
    <p class="abs quote">What can we say but thank you to Nerawave and Kelto Networks, they were able to quickly and effectively solve our WiFi problems. We had a very tight schedule to meet and they were able to get the results we needed. Now, several weeks later, we have logged more users and bandwidth usage on the network than ever before.</p>
    <div class="abs who"><b>-JONAS PELLERY</b><div>DIRECTOR OF CAPITAL PROJECTS AND FINANCE</div></div>
    <div class="abs tdots"><i></i><i class="on"></i><i></i><i></i><i></i></div>
  </section>

  <section class="abs news">
    <h2 class="abs news-title">LATEST NEWS</h2>
    <div class="abs news-sub">STAY TUNED</div>
    <article class="abs item" style="left:174px">
      <h5>What Customers<br>Time Sensitive</h5>
      <p>Lorem ipsum dolor sit amet, consectetur adipisicing elit, sed do eiusmod tempor incididunt ut labore et dolore magna aliqua. Ut enim ad minim veniam, quis nostrud exercitation ullamco laboris nisi ut aliquip ex ea commodo consequat.</p>
      <span class="btn">Read More</span>
    </article>
    <article class="abs item" style="left:320px">
      <h5>What Customers<br>Time Sensitive</h5>
      <p>Lorem ipsum dolor sit amet, consectetur adipisicing elit, sed do eiusmod tempor incididunt ut labore et dolore magna aliqua. Ut enim ad minim veniam, quis nostrud exercitation ullamco laboris nisi ut aliquip ex ea commodo consequat.</p>
      <span class="btn">Read More</span>
    </article>
    <article class="abs item" style="left:466px">
      <h5>Confidenceare<br>Saying About Us</h5>
      <p>Lorem ipsum dolor sit amet, consectetur adipisicing elit, sed do eiusmod tempor incididunt ut labore et dolore magna aliqua. Ut enim ad minim veniam, quis nostrud exercitation ullamco laboris nisi ut aliquip ex ea commodo consequat.</p>
      <span class="btn">Read More</span>
    </article>
  </section>

  <footer class="abs footer">
    <div class="abs fh" style="left:173px;top:23px">About Our Company</div>
    <div class="abs" style="left:173px;top:49px;display:flex;align-items:center;gap:4px">
      <span style="width:16px;height:16px;border-radius:50%;background:#fff"></span>
      <span style="font:700 11px 'Roboto Condensed',sans-serif;color:#fff">Vantrelo Alliance</span>
    </div>
    <p class="abs ftext" style="left:173px;top:76px;width:140px">Lorem ipsum dolor sit amet, consectetur adipisicing elit, sed do eiusmod tempor incididunt ut labore et dolore magna aliqua. Ut enim ad minim veniam, quis nostrud exercitation ullamco.</p>

    <div class="abs fh" style="left:351px;top:23px">Useful Links</div>
    <ul class="abs links" style="left:351px;top:45px">
      <li>Our Company</li><li>Freight Forwarding Services</li><li>Industry Specific Solutions</li><li>Express</li><li>Innovation</li><li>Contact Us</li>
    </ul>

    <div class="abs fh" style="left:466px;top:23px">Contact Info</div>
    <div class="abs ftext" style="left:466px;top:46px;width:160px"><span style="color:var(--green)">Address</span> : Halvard Logistic, Ostrow 12 Mill Lane, Ostrow<br><span style="color:var(--green)">Phone Number</span> : +00 20 5550 0142</div>
    <div class="abs" style="left:466px;top:78px;font:700 6.8px 'Roboto Condensed',sans-serif;color:#fff">NEWSLETTER</div>
    <div class="abs news-form"><span>Address Email</span><b>Subscribe</b></div>

    <div class="abs fline"></div>
    <div class="abs copy"><em>2015 VANTRELO ALLIANCE</em> - All Rights Reserved</div>
  </footer>

</div>
</body>
</html>
```